Maritime Law Firm Business Card Design Project

We are a new maritime law firm starting in Queensland, Australia. The principal is a master mariner as well as a lawyer and is looking for a logo design that evokes a practical and user-friendly approach to the law, as well as maritime law expertise.

We would like to use the compass rose as the foundation for the design, as it symbolises clarity of direction and purpose, as well as traditional maritime heritage.

The 16th Century Lluc Ferrandis Compass Rose (attached) is beautiful, but is too complex for a logo. A simplified version is desired.

Colour Paletter s flexible, although a B&W version is also needed. Colour suggestions are navy blue (for the sea), red and green (navigation lights) and maroon (for Queensland).

Target Market(s)

Maritime Industry/legal services

Industry/Entity Type

Law Firm

Font styles to use
Sans Serif

Requirements
Must have
• Contact Details
Name of 'Pellworth Legal'

```html
<!DOCTYPE html>
<html lang="en">
<head>
<meta charset="utf-8">
<title>Pellworth Legal – Business Cards</title>
<link href="https://fonts.googleapis.com/css2?family=Marcellus+SC&family=Open+Sans:wght@400;700&display=swap" rel="stylesheet">
<style>
  :root {
    --bg: #e9e6e1;
    --card-white: #fbfbfb;
    --navy: #3b3391;
    --navy-deep: #2a2274;
    --navy-light: #5650b0;
    --maroon: #9c1f24;
    --ink: #4a4a4a;
    --rule: #3b3391;
  }
  * { box-sizing: border-box; margin: 0; padding: 0; }
  html, body { width: 1200px; height: 1023px; overflow: hidden; }
  body {
    background: var(--bg);
    position: relative;
    font-family: "Open Sans", Arial, sans-serif;
  }
  .card {
    position: absolute;
    top: 356px;
    width: 540px;
    height: 310px;
    box-shadow: 0 6px 18px rgba(0,0,0,0.18);
  }
  /* Front */
  .card-front { left: 40px; background: var(--card-white); }
  .brand-mark {
    position: absolute; left: 36px; top: 56px;
    width: 44px; height: 44px; border-radius: 50%;
    background: var(--maroon);
  }
  .firm-name {
    position: absolute; left: 92px; top: 60px;
    font-family: "Marcellus SC", Georgia, serif;
    font-size: 29px; line-height: 36px; letter-spacing: 1px;
    color: var(--navy); white-space: nowrap;
  }
  .divider-vertical {
    position: absolute; left: 372px; top: 20px; bottom: 20px;
    width: 1px; background: var(--rule);
  }
  .person {
    position: absolute; left: 36px; top: 150px; width: 316px;
    display: flex; align-items: center; gap: 10px;
  }
  .person-name {
    font-family: "Marcellus SC", Georgia, serif;
    font-size: 22px; color: var(--maroon); white-space: nowrap;
  }
  .person-rule { flex: 1; height: 1px; background: var(--rule); }
  .person-title {
    position: absolute; left: 36px; top: 182px;
    font-size: 12px; color: var(--ink);
  }
  .contact-list {
    position: absolute; left: 36px; top: 212px;
    list-style: none; font-size: 12px; color: var(--ink);
  }
  .contact-list li { display: flex; align-items: center; gap: 10px; height: 22px; white-space: nowrap; }
  .contact-icon { width: 13px; height: 13px; }
  .address {
    position: absolute; left: 388px; top: 218px;
    font-size: 10px; font-weight: 700; line-height: 1.6; font-style: normal;
    color: var(--maroon); letter-spacing: 0.3px; text-transform: uppercase;
    white-space: nowrap;
  }
  /* Back */
  .card-back {
    left: 620px;
    background: linear-gradient(135deg, var(--navy-deep) 0%, var(--navy) 55%, var(--navy-light) 100%);
  }
  .back-lockup {
    position: absolute; inset: 0;
    display: flex; flex-direction: column; align-items: center; justify-content: center; gap: 26px;
  }
  .back-mark { width: 96px; height: 96px; border-radius: 50%; background: #ffffff; }
  .back-name {
    font-family: "Marcellus SC", Georgia, serif;
    font-size: 34px; letter-spacing: 1px; color: #ffffff; white-space: nowrap;
  }
</style>
</head>
<body>
  <section class="card card-front" aria-label="Business card front">
    <div class="brand-mark"></div>
    <div class="firm-name">Pellworth Legal</div>
    <div class="divider-vertical"></div>
    <div class="person">
      <span class="person-name">Maren Holloway</span>
      <span class="person-rule"></span>
    </div>
    <div class="person-title">Attorney at Law</div>
    <ul class="contact-list">
      <li>
        <svg class="contact-icon" viewBox="0 0 13 13"><rect width="13" height="13" rx="2" fill="#9c1f24"/><path d="M4 3.5l1.5 1.5-1 1c.6 1.2 1.3 1.9 2.5 2.5l1-1L9.5 9 8.5 10C6 9.5 3.5 7 3 4.5z" fill="#fff"/></svg>
        0400 615 272
      </li>
      <li>
        <svg class="contact-icon" viewBox="0 0 13 13"><rect width="13" height="13" rx="2" fill="#9c1f24"/><rect x="3" y="4" width="7" height="5" fill="none" stroke="#fff"/><path d="M3 4l3.5 3L10 4" fill="none" stroke="#fff"/></svg>
        maren@pellworthlegal.com
      </li>
      <li>
        <svg class="contact-icon" viewBox="0 0 13 13"><rect width="13" height="13" rx="2" fill="#9c1f24"/><circle cx="6.5" cy="6.5" r="3.5" fill="none" stroke="#fff"/><path d="M3 6.5h7M6.5 3v7" stroke="#fff"/></svg>
        www.pellworthlegal.com
      </li>
    </ul>
    <address class="address">PO Box 4120<br>Harbour Point<br>NSW Australia 2000</address>
  </section>

  <section class="card card-back" aria-label="Business card back">
    <div class="back-lockup">
      <div class="back-mark"></div>
      <div class="back-name">Pellworth Legal</div>
    </div>
  </section>
</body>
</html>
```